New Website for Consulting Company

Our company needs a fresh web design to help us drive our business forward. We are a consulting and software provider to Airports, Air Traffic Organizations, Builders and Architects. We specialize in analyzing operations, monitoring noise levels and creating software to improve operations, meet customer requirements and improve public relations.
Additional Info:
- Additional requirements can be found in the Web Design Brief
- Logo and logo branding attached
Target Market(s)
Airlines, Airports, Government Agencies, and Real Estate Developers
Industry/Entity Type
Aviation
Coding
Coded - Design and coding required
Number of Pages Required
2 page
Colors
Designer to choose colors to be used in the design.
Requirements
Must have
- - Create a Wordpress Design (Coded - Design and coding required)
- - Designer must provide full implementation/coding depending on the platform chosen by the client (i.e. Wordpress theme, HTML/CSS, etc.)
- - This is a multi-page site; Supporting pages can be formatted the same, but links need to be in place
- - Colors used must be grey scale, black or match the logo. It is not necessary to use all the colors in our logo
Should not have
- We are not looking for an overly bright site. While our logo has 5 different colors, it is not necessary to use all of them.

```html
<!DOCTYPE html>
<html lang="en">
<head>
<meta charset="utf-8">
<title>Aerolane Advisory — Consultants for Airlines and Airports</title>
<link rel="stylesheet" href="https://fonts.googleapis.com/css2?family=Fira+Sans:wght@300;400;500;600&family=Oswald:wght@400;500&display=swap">
<style>
:root{
  --blue:#1f74c6;
  --blue-dark:#1460ad;
  --green:#5fae3a;
  --lime:#8cc63f;
  --ink:#333;
  --muted:#666;
  --light:#f0f0f0;
  --grey:#e3e3e3;
  --yellow:#d9c541;
  --magenta:#b0306a;
  --sage:#9bb08c;
}
*{box-sizing:border-box;margin:0;padding:0}
html,body{width:1200px;height:1200px;overflow:hidden;background:#fff}
body{font-family:"Fira Sans",sans-serif;color:var(--ink)}
.page{position:absolute;left:345.6px;top:0;width:636px;height:1500px;transform:scale(.8);transform-origin:0 0;background:#fff}
.abs{position:absolute}

/* header */
.header{left:0;top:0;width:636px;height:23px;background:#fff}
.brand{left:62px;top:-30px;width:116px;height:78px;border-radius:50%;background:#fff;display:flex;align-items:flex-end;justify-content:center;padding-bottom:17px;z-index:3}
.brand span{font-weight:600;font-size:16px;color:#1b2b4a}
.nav{right:64px;top:3px;display:flex;gap:0;align-items:center}
.nav a{font-size:6.5px;color:#444;text-decoration:none;padding:0 7.5px;line-height:16px}
.nav a.cta{background:var(--blue);color:#fff;font-weight:600;padding:0 8px;margin-left:6px}

/* hero */
.hero{left:0;top:23px;width:636px;height:267px;background:linear-gradient(180deg,#6f86c4 0%,#a98ab6 28%,#d8a28e 40%,#575a7e 52%,#3b3f55 75%,#2c2f3e 100%)}
.hero-frame{left:56px;top:92px;width:220px;height:107px;border:1px solid rgba(255,255,255,.35)}
.hero h1{left:63px;top:36px;color:#fff;font-weight:400;line-height:1}
.hero h1 .l1{display:block;font-size:29px}
.hero h1 .l2{display:block;font-size:22px;font-weight:300;margin-top:1px}
.btn-quote{left:63px;top:113px;width:77px;height:19px;background:#fff;font-size:6.5px;color:#333;display:flex;align-items:center;justify-content:center}
.video-thumb{left:65px;top:170px;width:95px;height:65px;background:linear-gradient(180deg,#7a6a80,#3a3540);border:2px solid rgba(255,255,255,.5);display:flex;flex-direction:column;align-items:center;justify-content:center;gap:6px;color:#fff;font-size:6px}
.play{width:16px;height:16px;border-radius:50%;background:rgba(255,255,255,.85);position:relative}
.play::after{content:"";position:absolute;left:6px;top:4px;border-left:6px solid #333;border-top:4px solid transparent;border-bottom:4px solid transparent}
.hero-strip{left:0;top:287px;width:636px;height:3px;background:linear-gradient(90deg,var(--blue),var(--green),var(--yellow),var(--magenta))}
.orb{width:47px;height:47px;border-radius:50%;left:523px;display:flex;flex-direction:column;align-items:center;justify-content:center;color:#fff;font-size:5.5px;gap:3px;border:2px solid rgba(255,255,255,.6)}
.orb svg{width:12px;height:12px}
.orb.o1{top:32px;background:var(--blue)}
.orb.o2{top:85px;background:rgba(155,176,140,.85)}
.orb.o3{top:135px;background:rgba(217,197,65,.8)}
.orb.o4{top:187px;background:rgba(176,48,106,.8)}

/* intro */
.section-title{left:0;width:636px;text-align:center;color:var(--blue);font-size:13px;letter-spacing:1.2px;font-weight:400}
.lead{left:150px;width:336px;text-align:center;font-size:5.5px;line-height:10px;color:#444}
.lead u{color:var(--blue)}
.card{width:114px;top:371px}
.card .img{height:88px;background:linear-gradient(180deg,#9dbbd8,#5a6b7c)}
.card h3{margin-top:6px;font-size:8.5px;font-weight:400;color:#333;border-left:1.5px solid var(--blue);padding-left:3px;line-height:10px}
.card p{margin-top:4px;font-size:5px;line-height:10px;color:#555}
.card .more{position:absolute;right:0;top:133px;width:11px;height:11px;border:1px solid #999;border-radius:50%}
.card .more svg{width:9px;height:9px;position:absolute;left:0;top:0}

/* award banner */
.award{left:0;top:545px;width:636px;height:196px;background:linear-gradient(180deg,#2b4a77 0%,#6a7ea3 45%,#c39a77 70%,#3a3f55 100%)}
.award-box{left:55px;top:29px;width:291px;height:113px;border:1px solid rgba(255,255,255,.55);background:rgba(40,60,95,.35);padding:20px 8px 0 8px;color:#fff}
.award-badge{left:130px;top:-12px;width:24px;height:24px;border-radius:50%;border:1.5px solid #fff;background:#2f4c78}
.award-box h2{font-weight:400;font-size:12.5px}
.award-box p{margin-top:6px;font-size:5px;line-height:10.2px;text-align:justify}
.btn-green{left:10px;top:100px;width:67px;height:21px;background:var(--green);color:#fff;font-size:7px;display:flex;align-items:center;justify-content:center}

.band{left:0;width:636px;background:var(--blue);color:#fff}
.band-info{top:740px;height:41px;display:flex;align-items:center;justify-content:center;gap:10px;font-size:11.5px;letter-spacing:.3px}
.btn-outline{border:1.2px solid #fff;border-radius:10px;padding:0 25px;height:18px;line-height:16px;font-size:5.5px;font-weight:600}

/* testimonial */
.testimonial-text{z-index:2}
.t-label{left:104px;top:836px;font-family:"Oswald",sans-serif;font-size:7px;color:#777}
.t-line{left:104px;top:850px;width:326px;height:60px}
.t-quote{left:104px;top:856px;font-family:"Oswald",sans-serif;font-weight:500;font-size:15px;color:#333;white-space:nowrap}
.t-sub{left:213px;top:886px;font-family:"Oswald",sans-serif;font-size:7px;color:#777;white-space:nowrap}
.t-sub b{color:var(--lime);font-weight:400}
.dots{left:210px;top:936px;display:flex;gap:4px}
.dots i{width:6px;height:6px;border-radius:50%;background:#ddd;display:block}
.dots i.on{background:#999}
.portrait{left:380px;top:790px;width:164px;height:220px;background:linear-gradient(180deg,#f2e8df 0%,#d4b8a4 35%,#2d2d33 55%,#1e1e22 100%);border-radius:70px 70px 0 0;z-index:1}

/* gallery */
.gallery{left:0;top:1010px;width:636px;height:219px;background:linear-gradient(180deg,#e8e8e8,#f6f6f6 60%,#e6e6e6)}
.gallery h2{position:absolute;left:0;top:24px;width:636px;text-align:center;font-weight:400;font-size:11.5px;letter-spacing:1px;color:#333}
.vid{top:74px;width:158px;height:111px;background:#fff;padding:8px 0 0}
.vid .img{height:95px;background:linear-gradient(135deg,#35507a,#1f3050 60%,#2c4468);display:flex;align-items:center;justify-content:center}
.vid .ring{width:36px;height:36px;border-radius:50%;border:2px solid #fff;position:relative}
.vid .ring::after{content:"";position:absolute;left:13px;top:9px;border-left:12px solid #fff;border-top:8px solid transparent;border-bottom:8px solid transparent}

.band-cta{top:1229px;height:67px}
.cta-text{left:142px;top:16px;line-height:1}
.cta-text .a{display:block;font-size:12px;letter-spacing:.3px}
.cta-text .b{display:block;font-size:16px;font-weight:600;margin-top:4px}
.btn-pill{left:352px;top:21px;width:132px;height:25px;border-radius:13px;background:var(--green);font-size:7.5px;font-weight:600;display:flex;align-items:center;justify-content:center}

/* footer */
.footer{left:0;top:1296px;width:636px;height:176px;background:var(--light)}
.f-h{font-size:7px;color:var(--blue);font-weight:500}
.office{left:63px;top:28px;width:122px}
.office li{list-style:none;display:flex;gap:8px;font-size:5.3px;line-height:8.3px;color:#444;margin-top:8px}
.office li svg{flex:none;width:8px;height:8px}
.divider{top:20px;width:1px;height:125px;background:#ccc}
.fnav{left:207px;top:28px}
.fnav ul{margin-top:9px;list-style:none}
.fnav li{font-size:5.3px;line-height:11.8px;color:#444}
.tweets{left:320px;top:22px;width:114px;height:135px;background:#fff;padding:4px}
.tweets .th{font-size:6px;font-weight:600;color:#333;display:flex;justify-content:space-between}
.tweets .th span{font-size:4px;background:#e8eef5;padding:0 3px;font-weight:400}
.tw{display:flex;gap:5px;margin-top:8px}
.tw .av{flex:none;width:12px;height:12px;border-radius:50%;background:#55acee}
.tw .av.sq{border-radius:1px;background:#333}
.tw p{font-size:4.3px;line-height:5.6px;color:#444}
.tw p b{color:#222}
.tw p em{color:var(--blue);font-style:normal}
.f-brand{left:480px;top:74px;font-size:17px;font-weight:600;color:#1b2b4a}
.copy{left:0;top:1472px;width:636px;height:28px;background:var(--grey);font-size:5px;color:#555;display:flex;align-items:center;justify-content:center}
</style>
</head>
<body>
<div class="page">

  <header class="abs header">
    <div class="abs brand"><span>Aerolane</span></div>
    <nav class="abs nav">
      <a>Home</a><a>Airports</a><a>Airspace</a><a>Emissions</a><a>Acoustics</a><a>Visualization</a><a>About</a><a class="cta">CONTACT US</a>
    </nav>
  </header>

  <section class="abs hero" role="img" aria-label="Modern airport terminal at dusk with a jet flying overhead above the runway">
    <div class="abs hero-frame"></div>
    <h1 class="abs"><span class="l1">Consultants for</span><span class="l2">Airlines and Airports</span></h1>
    <div class="abs btn-quote">Request A Quote &gt;</div>
    <div class="abs video-thumb" role="img" aria-label="Video still of an aircraft on the apron"><div class="play"></div>Play this Video</div>
    <div class="abs orb o1"><svg viewBox="0 0 12 12"><circle cx="6" cy="6" r="4" fill="none" stroke="#fff" stroke-width="1.4"/></svg>Consultants</div>
    <div class="abs orb o2"><svg viewBox="0 0 12 12"><path d="M2 10V5h3v5M6 10V2h4v8" fill="none" stroke="#fff"/></svg>Airports</div>
    <div class="abs orb o3"><svg viewBox="0 0 12 12"><path d="M1 6h10M7 3l4 3-4 3" fill="none" stroke="#fff"/></svg>Airspace</div>
    <div class="abs orb o4"><svg viewBox="0 0 12 12"><rect x="3.5" y="1" width="5" height="10" rx="1" fill="none" stroke="#fff"/></svg>Contact Us</div>
  </section>
  <div class="abs hero-strip"></div>

  <h2 class="abs section-title" style="top:312px">AEROLANE ADVISORY INVENTS AND DEPLOYS</h2>
  <p class="abs lead" style="top:332px">Aerolane Advisory invents and deploys innovative management and technology solutions that address complex noise and airspace issues for airports and residential communities. <u>Read More &gt;&gt;</u></p>

  <article class="abs card" style="left:63px"><div class="img" role="img" aria-label="Aircraft parked at an airport terminal gate"></div><h3>AIRPORTS</h3><p>Lorem ipsum dolor sit amet, consectetur adipiscing elit, sed do eiusmod tempor.</p><span class="more"><svg viewBox="0 0 9 9"><path d="M2.5 4.5h4M5 3l1.5 1.5L5 6" fill="none" stroke="#999" stroke-width=".8"/></svg></span></article>
  <article class="abs card" style="left:194px"><div class="img" style="background:linear-gradient(135deg,#e6e9ee,#a9b6c6)" role="img" aria-label="Hand using a tablet showing charts"></div><h3>SOFTWARE</h3><p>Lorem ipsum dolor sit amet, consectetur adipiscing elit, sed do eiusmod tempor.</p><span class="more"><svg viewBox="0 0 9 9"><path d="M2.5 4.5h4M5 3l1.5 1.5L5 6" fill="none" stroke="#999" stroke-width=".8"/></svg></span></article>
  <article class="abs card" style="left:326px"><div class="img" style="background:linear-gradient(180deg,#6fa6d8,#cfe3f2 55%,#1d2a36 80%)" role="img" aria-label="Travellers watching a jet take off through terminal windows"></div><h3>NOISE &amp; EMISSIONS</h3><p>Lorem ipsum dolor sit amet, consectetur adipiscing elit, sed do eiusmod tempor.</p><span class="more"><svg viewBox="0 0 9 9"><path d="M2.5 4.5h4M5 3l1.5 1.5L5 6" fill="none" stroke="#999" stroke-width=".8"/></svg></span></article>
  <article class="abs card" style="left:457px"><div class="img" style="background:linear-gradient(180deg,#bdbdbd,#4a4a4a)" role="img" aria-label="Black and white airport lounge with seating"></div><h3>VISUALIZATION</h3><p>Lorem ipsum dolor sit amet, consectetur adipiscing elit, sed do eiusmod tempor.</p><span class="more"><svg viewBox="0 0 9 9"><path d="M2.5 4.5h4M5 3l1.5 1.5L5 6" fill="none" stroke="#999" stroke-width=".8"/></svg></span></article>

  <section class="abs award" role="img" aria-label="Jet airliner on approach at dusk over blurred city lights">
    <div class="abs award-box">
      <div class="abs award-badge"></div>
      <h2>NOVIS WINS 2012 SOFTWARE INNOVATION!!</h2>
      <p>NOVIS is a web-based application designed to create, evaluate and display flight operations in 3D. This software tool evaluates the acoustic and environmental impacts from new Performance Based Procedures as well as new runway and airfield configurations, providing a display of noise impacts using various acoustic parameters including A-weighted noise levels and audibility detection. NOVIS can be used for all classes of aircraft operations ranging from commercial jets on a single runway to metroplex operations.</p>
      <div class="abs btn-green">READ MORE</div>
    </div>
  </section>
  <div class="abs band band-info">TO KNOW MORE INFORAMATION OR OUR PORTFOLIO <span class="btn-outline">REQUEST A QUOTE</span></div>

  <div class="abs portrait" role="img" aria-label="Portrait of a smiling client executive in a dark suit with arms folded"></div>
  <div class="abs t-label testimonial-text">AEROLANE ADVISORY NEW AIRPORT</div>
  <svg class="abs t-line testimonial-text" viewBox="0 0 326 60"><path d="M0 1H290L326 38" fill="none" stroke="var(--lime)" stroke-width="1.2"/></svg>
  <div class="abs t-quote testimonial-text">“ VERY VERY GOOD WORK AND I AM HAPPY ”</div>
  <div class="abs t-sub testimonial-text">-AEROLANE ADVISORY IS <b>CEO OF NEW AIRPORT</b></div>
  <div class="abs dots testimonial-text"><i></i><i class="on"></i><i></i></div>

  <section class="abs gallery">
    <h2>FEATURES VIDEO GALLERY</h2>
    <p class="abs lead" style="left:160px;width:316px;top:43px">Aerolane Advisory invents and deploys innovative management and technology solutions that address complex noise and airspace issues for airports and residential communities. <u>Read More &gt;&gt;</u></p>
    <div class="abs vid" style="left:63px"><div class="img" role="img" aria-label="Video still of a satellite map with flight profile labels"><span class="ring"></span></div></div>
    <div class="abs vid" style="left:237px"><div class="img" role="img" aria-label="Video still of a satellite map with flight profile labels"><span class="ring"></span></div></div>
    <div class="abs vid" style="left:414px"><div class="img" role="img" aria-label="Video still of a satellite map with flight profile labels"><span class="ring"></span></div></div>
  </section>

  <section class="abs band band-cta">
    <div class="abs cta-text"><span class="a">OUR CLIENT CALL US THEIR</span><span class="b">IN - HOUSE CONSULTANT</span></div>
    <div class="abs btn-pill">REQUEST A QUOTE &gt;</div>
  </section>

  <footer class="abs footer">
    <div class="abs office">
      <div class="f-h">AEROLANE OFFICE</div>
      <ul>
        <li><svg viewBox="0 0 8 8"><path d="M4 7.5C2 5 1.5 4 1.5 3a2.5 2.5 0 015 0c0 1-.5 2-2.5 4.5z" fill="var(--green)"/></svg><span>Aerolane Advisory<br>4120 Harbor Crest Drive, Suite<br>310 Bayfield,<br>California 90210</span></li>
        <li style="margin-top:10px"><svg viewBox="0 0 8 8"><path d="M1.5 1h2l.7 1.8-1 .7a4 4 0 002.3 2.3l.7-1L7 5.5v2C3.5 7.5.5 4.5.5 1z" fill="var(--green)"/></svg><span>Phone: +1 (555) 410-2200</span></li>
        <li style="margin-top:4px"><svg viewBox="0 0 8 8"><rect x="1" y="2" width="6" height="5" fill="var(--green)"/></svg><span>Fax: +1 (555) 410-2205</span></li>
        <li style="margin-top:10px"><svg viewBox="0 0 8 8"><rect x=".5" y="1.5" width="7" height="5" fill="var(--green)"/><path d="M.5 1.5L4 4.5l3.5-3" fill="none" stroke="#fff" stroke-width=".6"/></svg><span>info@aerolane-example.com</span></li>
      </ul>
    </div>
    <div class="abs divider" style="left:187px"></div>
    <div class="abs fnav">
      <div class="f-h">NAVIGATION</div>
      <ul><li>Home</li><li>Airports</li><li>Airspace</li><li>Emissions</li><li>Acoustics</li><li>Visualization</li><li>About</li></ul>
    </div>
    <div class="abs divider" style="left:287px"></div>
    <div class="abs tweets">
      <div class="th">Tweets <span>Follow</span></div>
      <div class="tw"><span class="av"></span><p><b>Newsfeed</b> @newsfeed<br>We're testing commerce on the feed. Please read our updated Terms and Privacy Policy <em>newsfeed.example/privacy</em><br>Expand</p></div>
      <div class="tw"><span class="av"></span><p><b>Newsfeed</b> @newsfeed<br>A new way for you to discover and buy products on the feed. <em>blog.newsfeed.example/2014/testing</em><br>Show Summary</p></div>
      <div class="tw"><span class="av sq"></span><p><b>Style Feed</b> @stylefeed<br>This is how much we love our exclusive fashion offers <em>blog.newsfeed.example/2014/style</em> Thank you <em>pic.newsfeed.example/x1</em><br>Retweeted by Newsfeed</p></div>
    </div>
    <div class="abs f-brand">Aerolane</div>
  </footer>
  <div class="abs copy">©2017 Aerolane Advisory. All Rights Reserved.</div>

</div>
</body>
</html>
```